Mailer Postcard for Potential Bankruptcy Clients

The postcard will be printed at 8.5"x6" to abide by the specification at the following link: https://www.mailvortex.example/art-upload/guide/. I want an attractive two sided post card that includes my logo (see attachment). The design would have to have room for the website address, phone number, two location addresses and give them information about a civil action pending against them (You are being sued in X county (case# xxyx). We can help.). I don't really like the visuals of the attached postcard, so please use as a general guide for what I am trying to do. Ultimately, I want an ad that gets people to call me so I can help them.

I also want it to be compatible with the website (CreditHarbor.Legal).

Target Market(s)

Potential bankruptcy clients.

Industry/Entity Type

Legal

Colors

Designer to choose colors to be used in the design.

Requirements
Must have
• Phone number, addresses, website, and place for text regarding pending legal action against the receiver. Should say something to the effect: You have a pending legal action in (county name) County (court name [superior, magistrate, ect.]). Let us help you deal with it responsibly.
• Please note the design specifications at this link:

```html
<!DOCTYPE html>
<html lang="en">
<head>
<meta charset="utf-8">
<title>Credit Harbor Law Group – Mailer Postcard</title>
<link href="https://fonts.googleapis.com/css2?family=Roboto:ital,wght@0,400;0,500;0,700;0,900;1,700;1,900&family=Roboto+Condensed:wght@400;500;700&display=swap" rel="stylesheet">
<style>
  :root{
    --page:#e9e6e2;
    --white:#ffffff;
    --ink:#111111;
    --grey-panel:#e4e4e4;
    --green:#63c45c;
    --red:#9b1f1f;
    --red-band:#8c1b15;
    --orange:#f0a93c;
    --photo-light:#8a8a8a;
    --photo-dark:#2a2a2a;
    --black-band:#0d0d0d;
    --logo-grey:#4a4a4a;
  }
  *{margin:0;padding:0;box-sizing:border-box}
  html,body{width:1200px;height:474px;overflow:hidden;background:var(--page)}
  body{position:relative;font-family:"Roboto",sans-serif;color:var(--ink)}

  .card{position:absolute;top:33px;height:397px;background:var(--white);overflow:hidden;box-shadow:0 2px 6px rgba(0,0,0,.25)}
  .card--front{left:35px;width:553px}
  .card--back{left:621px;width:546px}

  /* front */
  .case-box{position:absolute;left:0;top:0;width:203px;height:94px;background:var(--grey-panel);
    font:500 15.5px/1.3 "Roboto",sans-serif;text-align:center;padding-top:12px}
  .headline-band{position:absolute;left:203px;top:0;width:350px;height:94px;background:var(--green);
    color:var(--white);font:italic 900 44px/94px "Roboto",sans-serif;padding-left:20px;letter-spacing:.5px;white-space:nowrap}
  .photo{position:absolute;left:0;top:94px;width:553px;height:213px;
    background:linear-gradient(100deg,var(--photo-light) 0%,#5c5752 35%,var(--photo-dark) 60%,#6b6b6b 100%)}
  .offer-badge{position:absolute;left:32px;top:120px;width:132px;height:132px;border-radius:50%;
    background:var(--red);color:var(--white);font:700 18px/1.25 "Roboto Condensed",sans-serif;
    text-align:center;display:flex;align-items:center;justify-content:center}
  .warning-band{position:absolute;left:0;top:307px;width:350px;height:22px;background:var(--red-band);
    color:var(--white);font:700 11.5px/22px "Roboto Condensed",sans-serif;text-align:center;white-space:nowrap}
  .cta{position:absolute;left:0;top:329px;width:350px;height:68px;background:var(--orange);text-align:center}
  .cta__lead{font:400 13px/1 "Roboto",sans-serif;margin-top:7px}
  .cta__phone{font:700 22px/1 "Roboto",sans-serif;color:var(--red-band);margin-top:4px;display:flex;justify-content:center;align-items:center;gap:6px}
  .cta__web{font:700 14px/1 "Roboto",sans-serif;margin-top:5px}
  .brand-panel{position:absolute;left:350px;top:307px;width:203px;height:90px;background:var(--grey-panel)}

  .brand{position:absolute;display:flex;align-items:center;gap:9px}
  .brand__mark{width:22px;height:22px;background:var(--green);flex:none}
  .brand__name{font:400 19px/1.1 "Roboto",sans-serif;color:var(--logo-grey);white-space:nowrap}
  .brand-panel .brand{left:30px;top:23px}

  /* back */
  .back-headline{position:absolute;left:18px;top:12px;font:italic 900 24.5px/1.12 "Roboto",sans-serif;white-space:nowrap}
  .postage{position:absolute;right:6px;top:8px;width:70px;height:64px;border:1px solid var(--ink);
    font:400 6px/1.3 "Roboto",sans-serif;text-align:center;padding-top:10px}
  .intro{position:absolute;left:24px;top:78px;width:310px;font:400 10px/1.25 "Roboto Condensed",sans-serif}
  .benefits{position:absolute;left:74px;top:132px;list-style:none;font:500 12.5px/18.5px "Roboto",sans-serif;white-space:nowrap}
  .benefits li::before{content:"•";margin-right:6px}
  .benefits li:nth-child(n+6){font-weight:700}
  .back-cta{position:absolute;left:70px;top:274px;width:175px;text-align:center}
  .back-cta__lead{font:500 12px/1 "Roboto",sans-serif}
  .back-cta__phone{font:500 18px/1 "Roboto",sans-serif;margin-top:7px}
  .back-cta__web{font:500 12px/1 "Roboto",sans-serif;margin-top:4px}
  .disclaimer{position:absolute;left:40px;top:352px;width:280px;font:400 5.5px/1.35 "Roboto",sans-serif}
  .card--back .brand{left:348px;top:88px}
  .address-band{position:absolute;left:272px;top:142px;width:274px;height:29px;background:var(--black-band);
    color:var(--white);display:flex;font:700 7.5px/1.3 "Roboto Condensed",sans-serif}
  .address{padding:4px 6px 0;white-space:nowrap}
  .address + .address{border-left:1px solid var(--white)}
</style>
</head>
<body>
  <section class="card card--front">
    <div class="case-box">You are being sued in<br>__________ County<br>case # ____________</div>
    <div class="headline-band">WE CAN HELP</div>
    <div class="photo" role="img" aria-label="Photo of a stressed man in a suit holding his head in his hands at an office desk"></div>
    <div class="offer-badge">$0 DOWN<br>BANKRUPTCY<br>OPTIONS</div>
    <div class="warning-band">DON'T LET THEM FORECLOSE, SUE OR GARNISH YOUR WAGES!</div>
    <div class="cta">
      <p class="cta__lead">CALL NOW for a FREE Consultation.</p>
      <p class="cta__phone">
        <svg width="18" height="18" viewBox="0 0 24 24" aria-hidden="true"><circle cx="12" cy="12" r="11" fill="none" stroke="#8c1b15" stroke-width="2"/><path d="M8 7c1-1 2 0 2.5 1.5s-1 1.5-.5 2.5 2 2.5 3 3 1-1 2.5-.5S16.5 16 15.5 17c-2 1.5-9-5.5-7.5-10z" fill="#8c1b15"/></svg>
        (404) 555.0182
      </p>
      <p class="cta__web">www.creditharbor.legal</p>
    </div>
    <div class="brand-panel">
      <div class="brand"><span class="brand__mark"></span><span class="brand__name">Credit Harbor<br>Law Group</span></div>
    </div>
  </section>

  <section class="card card--back">
    <h2 class="back-headline">If you qualify, you can file<br>bankruptcy for $0 upfront!</h2>
    <div class="postage">Presorted<br>STANDARD U.S. Postage<br><b>PAID</b><br>Atlanta, GA<br>Permit No. XXX</div>
    <p class="intro">We file both Chapter 7 (Liquidation) and Chapter 13 (wage-earners repayment plans) for our clients depending on their individual situation. Bankruptcy is a powerful tool to stop creditors in their tracks immediately.</p>
    <ul class="benefits">
      <li>Affordable Re-Payment Plans</li>
      <li>No-Money Down Options</li>
      <li>Evening &amp; Weekend Hours</li>
      <li>No Need to Miss Work!</li>
      <li>Child Friendly Office</li>
      <li>Bankruptcy Expertise</li>
      <li>It's All We Do!</li>
    </ul>
    <div class="back-cta">
      <p class="back-cta__lead">Call Today!</p>
      <p class="back-cta__phone">(404) 555-0182</p>
      <p class="back-cta__web">www.creditharbor.legal</p>
    </div>
    <p class="disclaimer">The choice of a lawyer is an important one and should not be based solely on advertising. Credit Harbor Law Group is a debt relief agency and helps its clients seek relief under the federal bankruptcy code. Credit Harbor Law Group is licensed in federal bankruptcy courts and in the state of Georgia.</p>
    <div class="brand"><span class="brand__mark"></span><span class="brand__name">Credit Harbor<br>Law Group</span></div>
    <div class="address-band">
      <p class="address">418 Linden Ave., NE Suite #310<br>Atlanta, Georgia 30308</p>
      <p class="address">5512 Maple Row Douglasville,<br>Georgia 30135</p>
    </div>
  </section>
</body>
</html>
```